Corvel Ridge New Website Design

We just changed our logo (thank you PlanHarbor) and company name change from Corvel Ridge Machining to Corvel Ridge Manufacturing. We do CNC Swiss screw machining and multi-axis machines. We make parts for many industries. We make large quantity production parts as well small R&D quantities. You can look at our current (outdated) website: http://www.corvelridgemachining.example to see what we do. We would like a WordPress site, including contact form for "request for quote" . We would also like it to be mobile friendly, and the ability to maintain it ourselves after it is finished I have included our new logo and fonts for references. We would like our site to convey the feeling of precision, capability, and trust worthiness with a very modern look. The new website address is www.corvelridge-mfg.example

Coding

Coded - Design and coding required

Number of Pages Required

5+ page

Font styles to use
Serif
Sans Serif
Other font styles liked:
• fronts included, not sure if they work

Colors

Designer to choose colors to be used in the design.

Requirements
Must have
• Contact Info, request for quote field

```html
<!DOCTYPE html>
<html lang="en">
<head>
<meta charset="utf-8">
<title>Corvel Ridge Manufacturing</title>
<link href="https://fonts.googleapis.com/css2?family=Mulish:ital,wght@0,300;0,400;0,600;0,700;1,400&display=swap" rel="stylesheet">
<style>
:root{
  --navy:#2b4593;
  --navy-deep:#25397d;
  --orange:#f3904f;
  --ink:#2a2f3a;
  --text:#6b6f78;
  --muted:#8a8e96;
  --line:#d5d8de;
  --paper:#ffffff;
  --tint:#f6f6f7;
  --foot-bar:#ededee;
}
*{box-sizing:border-box;margin:0;padding:0}
html,body{width:1200px;height:3042px;overflow:hidden;background:var(--paper)}
body{font-family:'Mulish',sans-serif;color:var(--text);position:relative}
.abs{position:absolute}

/* header */
.site-header{position:absolute;left:0;top:0;width:1200px;height:104px;background:var(--paper)}
.brand{position:absolute;left:77px;top:34px;display:flex;align-items:center;gap:10px;font-size:24px;font-weight:700;color:var(--navy);letter-spacing:.5px}
.brand-dot{width:14px;height:14px;border-radius:50%;background:var(--navy)}
.main-nav{position:absolute;right:110px;top:44px;display:flex;gap:26px;font-size:14px;color:#555a63;letter-spacing:.3px}
.main-nav .active{color:var(--navy);position:relative}
.main-nav .active::before{content:"";position:absolute;left:0;top:-8px;width:22px;height:2px;background:var(--navy)}
.search{position:absolute;left:1102px;top:41px}

/* hero */
.hero{position:absolute;left:0;top:104px;width:1200px;height:552px;overflow:hidden}
.hero-photo{position:absolute;inset:0;background:linear-gradient(120deg,#3a3b3d 0%,#9a9b9d 35%,#cfd0d1 55%,#6f7072 80%,#444 100%)}
.hero svg{position:absolute;inset:0}
.hero-title{position:absolute;right:80px;top:116px;text-align:right;color:#fff;font-size:38px;font-weight:600;line-height:48px;letter-spacing:.5px}

/* industries */
.section-title{position:absolute;left:0;width:1200px;text-align:center;font-size:36px;font-weight:600;color:var(--ink);letter-spacing:.5px}
.industry{position:absolute;width:240px;height:219px;background:var(--paper);box-shadow:0 2px 12px rgba(0,0,0,.08);border-bottom:4px solid var(--navy);text-align:center}
.industry svg{position:absolute;left:88px;top:54px}
.industry span{position:absolute;left:0;right:0;top:140px;font-size:20px;color:#3a3d44}

/* features */
.features{position:absolute;left:0;top:1354px;width:1200px;height:700px;background:var(--tint)}
.card{position:absolute;background:var(--paper);box-shadow:0 1px 8px rgba(0,0,0,.05)}
.card-photo{position:absolute}
.card h3{position:absolute;font-size:21px;font-weight:700;color:var(--navy);letter-spacing:.3px}
.card p{position:absolute;font-size:13.5px;line-height:25px;color:var(--text)}
.btn{position:absolute;background:var(--orange);color:#fff;font-size:13px;font-weight:700;padding:0 11px;height:30px;line-height:30px}

/* testimonials band */
.band{position:absolute;left:0;top:2030px;width:1200px;height:650px}
.testimonials h2{position:absolute;left:79px;top:2215px;color:#fff;font-size:36px;font-weight:600}
.quote-mark{position:absolute;left:78px;top:2280px;width:68px;height:68px;border:2px solid #fff;border-radius:50%}
.quote-text{position:absolute;left:79px;top:2368px;width:520px;color:#fff;font-style:italic;font-size:18px;line-height:30px}
.author{position:absolute;left:79px;top:2450px;color:#fff;font-size:18px;font-weight:700}
.role{position:absolute;left:79px;top:2484px;color:#fff;font-size:13px}

.quote-form{position:absolute;left:665px;top:2063px;width:457px;height:541px;background:var(--paper)}
.quote-form h2{position:absolute;left:0;right:0;top:55px;text-align:center;font-size:27px;font-weight:700;color:var(--ink)}
.field{position:absolute;left:36px;width:385px;height:42px;border:1px solid var(--line);font-size:13.5px;color:#777;padding:12px 17px}
.send{position:absolute;left:36px;top:430px;width:385px;height:41px;background:var(--orange);color:#fff;text-align:center;line-height:41px;font-size:18px;font-weight:700}

/* footer */
.badge{position:absolute}
.footer-about{position:absolute;left:79px;top:2818px;width:240px;font-size:13.5px;line-height:25px;color:var(--text)}
.foot-title{position:absolute;font-size:21px;font-weight:600;color:var(--ink)}
.sitemap{position:absolute;list-style:none;font-size:13.5px;color:var(--text)}
.sitemap li{height:37px;padding-left:18px;position:relative}
.sitemap li::before{content:"";position:absolute;left:0;top:6px;width:7px;height:7px;border-radius:50%;background:var(--navy)}
.contact-row{position:absolute;left:885px;font-size:13.5px;line-height:25px;color:var(--text)}
.contact-row svg{position:absolute;left:0;top:4px}
.contact-row span{display:block;padding-left:30px}
.copyright{position:absolute;left:0;top:2985px;width:1200px;height:57px;background:var(--foot-bar);text-align:center;font-size:13.5px;line-height:57px;color:#555}
</style>
</head>
<body>

<header class="site-header">
  <div class="brand"><span class="brand-dot"></span>CORVEL RIDGE</div>
  <nav class="main-nav">
    <span class="active">HOME</span><span>SERVICES</span><span>EQUIPMENT</span><span>QUALITY</span><span>OUR WORK</span><span>ABOUT US</span><span>CONTACT US</span>
  </nav>
  <svg class="search" width="22" height="22" viewBox="0 0 22 22"><circle cx="9" cy="9" r="7" fill="none" stroke="#333" stroke-width="2.6"/><line x1="14" y1="14" x2="20" y2="20" stroke="#333" stroke-width="2.8" stroke-linecap="round"/></svg>
</header>

<section class="hero">
  <div class="hero-photo" role="img" aria-label="Close-up of a CNC milling tool cutting an aluminium part"></div>
  <svg width="1200" height="552" viewBox="0 0 1200 552">
    <polygon points="1105,0 1200,0 1200,552 605,552" fill="#3b3c3e" opacity=".88"/>
    <polygon points="890,300 1200,300 1045,552" fill="var(--orange)"/>
  </svg>
  <div class="hero-title">QUALITY -<br>FROM INCEPTION<br>TO COMPLETION</div>
</section>

<h2 class="section-title" style="top:712px">INDUSTRIES SERVED</h2>

<div class="industry" style="left:77px;top:790px">
  <svg width="64" height="64" viewBox="0 0 64 64" fill="none" stroke="#777" stroke-width="1.6"><path d="M10 54 L24 40 M40 8 C50 4 58 6 56 14 C54 22 40 36 30 44 L20 34 C28 24 32 12 40 8Z M20 34 L10 32 L16 26 L28 26 M30 44 L32 54 L38 48 L38 36"/><circle cx="44" cy="18" r="4"/></svg>
  <span>Aerospace</span>
</div>
<div class="industry" style="left:346px;top:790px">
  <svg width="64" height="64" viewBox="0 0 64 64" fill="none" stroke="#777" stroke-width="1.6"><rect x="12" y="12" width="40" height="40" rx="3"/><rect x="18" y="18" width="28" height="28"/><path d="M18 4v8M26 4v8M34 4v8M42 4v8M18 52v8M26 52v8M34 52v8M42 52v8M4 20h8M4 28h8M4 36h8M4 44h8M52 20h8M52 28h8M52 36h8M52 44h8"/></svg>
  <span>Electronics</span>
</div>
<div class="industry" style="left:614px;top:790px">
  <svg width="64" height="64" viewBox="0 0 64 64" fill="none" stroke="#777" stroke-width="1.6"><circle cx="32" cy="32" r="28"/><circle cx="32" cy="32" r="22"/><circle cx="32" cy="32" r="5"/><circle cx="32" cy="18" r="4"/><circle cx="20" cy="38" r="4"/><circle cx="44" cy="38" r="4"/></svg>
  <span>Automotive</span>
</div>
<div class="industry" style="left:883px;top:790px">
  <svg width="64" height="64" viewBox="0 0 64 64" fill="none" stroke="#777" stroke-width="1.6"><circle cx="32" cy="10" r="5"/><path d="M32 15 V58 M22 24 H42 M8 40 C10 52 22 58 32 58 C42 58 54 52 56 40 M4 44 L8 38 L13 44 M51 44 L56 38 L60 44"/></svg>
  <span>Marine</span>
</div>
<div class="industry" style="left:210px;top:1048px">
  <svg width="64" height="64" viewBox="0 0 64 64" fill="none" stroke="#777" stroke-width="1.6"><rect x="2" y="8" width="60" height="40" rx="2"/><rect x="8" y="14" width="48" height="28"/><path d="M26 48 L24 58 M38 48 L40 58 M18 58 H46 M26 30h12" stroke-dasharray="2 2"/></svg>
  <span>Computer</span>
</div>
<div class="industry" style="left:480px;top:1048px">
  <svg width="64" height="64" viewBox="0 0 64 64" fill="none" stroke="#777" stroke-width="1.6"><path d="M32 58 C10 42 2 30 4 18 C6 8 20 4 32 16 C44 4 58 8 60 18 C62 30 54 42 32 58Z"/><path d="M8 34 H20 L24 26 L30 42 L34 30 L38 36 H56"/></svg>
  <span>Medical</span>
</div>
<div class="industry" style="left:750px;top:1048px">
  <svg width="64" height="64" viewBox="0 0 64 64" fill="none" stroke="#777" stroke-width="1.6"><path d="M18 4 C8 4 6 14 8 24 C10 34 14 38 16 50 C17 58 22 62 24 58 C26 52 26 40 32 40 C38 40 38 52 40 58 C42 62 47 58 48 50 C50 38 54 34 56 24 C58 14 56 4 46 4 C40 4 36 8 32 8 C28 8 24 4 18 4Z"/><path d="M14 12 C14 10 16 8 19 8"/></svg>
  <span>Dental</span>
</div>

<section class="features">
  <div class="card" style="left:77px;top:92px;width:510px;height:500px">
    <div class="card-photo" role="img" aria-label="Polished metal gears meshing together" style="left:10px;top:10px;width:490px;height:291px;background:linear-gradient(135deg,#6b5a3c 0%,#c9c3b4 40%,#9a8350 65%,#3c3a36 100%)"></div>
    <h3 style="left:12px;top:327px">SERVICES</h3>
    <p style="left:12px;top:360px;width:470px">Providing you with honest straightforward service is our number one goal.We manufacture finished metal and plastic goods to tight...</p>
    <span class="btn" style="left:12px;top:432px">READ MORE</span>
  </div>
  <div class="card" style="left:612px;top:92px;width:510px;height:239px">
    <div class="card-photo" role="img" aria-label="CNC end mill machining an aluminium part" style="left:10px;top:10px;width:250px;height:219px;background:linear-gradient(135deg,#2e2f31 0%,#8a8b8d 50%,#c9cacb 75%,#555 100%)"></div>
    <h3 style="left:290px;top:34px">OUR WORK</h3>
    <p style="left:290px;top:73px;width:205px">Corvel Ridge has provided some of the most innovative results for clients, among many...</p>
    <span class="btn" style="left:290px;top:170px">READ MORE</span>
  </div>
  <div class="card" style="left:612px;top:352px;width:510px;height:239px">
    <div class="card-photo" role="img" aria-label="Lathe chuck and cutting tool inside a CNC machine" style="left:10px;top:10px;width:250px;height:219px;background:linear-gradient(135deg,#3a3b3d 0%,#a8a9ab 45%,#d9c66a 55%,#6c6d70 80%,#2f3032 100%)"></div>
    <h3 style="left:290px;top:34px">QUALITY</h3>
    <p style="left:290px;top:73px;width:205px">Corvel Ridge Machining recognizes that the disciplines of quality, health and safety...</p>
    <span class="btn" style="left:290px;top:170px">READ MORE</span>
  </div>
</section>

<div class="band" role="img" aria-label="Blue-tinted photo of a machined threaded part">
  <svg width="1200" height="650" viewBox="0 0 1200 650">
    <defs><linearGradient id="bandShade" x1="0" y1="0" x2="1" y2="1"><stop offset="0" stop-color="#3a55a3"/><stop offset=".5" stop-color="#2c4591"/><stop offset="1" stop-color="#253c82"/></linearGradient></defs>
    <polygon points="0,10 700,30 1200,110 1200,650 0,650" fill="url(#bandShade)"/>
  </svg>
</div>

<section class="testimonials">
  <h2>TESTIMONIALS</h2>
  <div class="quote-mark"><svg width="68" height="68" viewBox="0 0 68 68"><path d="M22 42 V34 C22 28 26 25 30 24 V28 C27 29 26 31 26 34 H30 V42Z M34 42 V34 C34 28 38 25 42 24 V28 C39 29 38 31 38 34 H42 V42Z" fill="var(--orange)" transform="translate(-2,0)"/></svg></div>
  <p class="quote-text">"I love working with engineers. Finding ways to make their parts less expensive is a puzzle I never get tired of solving."</p>
  <div class="author">Tomas Wendell</div>
  <div class="role">Founder</div>
</section>

<form class="quote-form">
  <h2>REQUEST A QUOTE</h2>
  <div class="field" style="top:107px">Name</div>
  <div class="field" style="top:161px">Email</div>
  <div class="field" style="top:215px">Phone</div>
  <div class="field" style="top:269px">Subject</div>
  <div class="field" style="top:323px;height:94px">Message</div>
  <div class="send">SEND</div>
</form>

<footer>
  <div class="badge" style="left:77px;top:2738px;width:78px;height:60px;background:var(--navy)"></div>
  <div class="badge" style="left:178px;top:2736px;width:64px;height:64px;border-radius:50%;background:#e4e4e6;border:2px solid #b8b8bb"></div>
  <p class="footer-about">Corvel Ridge Machining Company is a high quality machining resource providing friendly service, fast turnaround times, and engineering.</p>

  <div class="foot-title" style="left:410px;top:2732px">SITEMAP</div>
  <ul class="sitemap" style="left:410px;top:2780px"><li>Home</li><li>Services</li><li>Quality</li><li>Our Work</li></ul>
  <ul class="sitemap" style="left:617px;top:2780px"><li>About us</li><li>Contact us</li><li>Sitemap</li><li>Privacy policy</li></ul>

  <div class="foot-title" style="left:885px;top:2732px">CONTACT INFO</div>
  <div class="contact-row" style="top:2775px"><svg width="16" height="20" viewBox="0 0 16 20"><path d="M8 0 C3.5 0 0 3.5 0 8 C0 13 8 20 8 20 C8 20 16 13 16 8 C16 3.5 12.5 0 8 0Z" fill="var(--orange)"/><circle cx="8" cy="8" r="3" fill="#fff"/></svg><span>4410 Halvern Ave. Brookvale,<br>CA 90000</span></div>
  <div class="contact-row" style="top:2836px"><svg width="18" height="18" viewBox="0 0 18 18"><path d="M4 1 L7 5 L5 7 C6 10 8 12 11 13 L13 11 L17 14 L15 17 C8 17 1 10 1 3Z" fill="var(--orange)"/></svg><span>555-014-2290</span></div>
  <div class="contact-row" style="top:2873px"><svg width="18" height="14" viewBox="0 0 18 14"><rect width="18" height="14" rx="1" fill="var(--orange)"/><path d="M1 1 L9 8 L17 1" fill="none" stroke="#fff" stroke-width="1.4"/></svg><span>info@corvelridge-mfg.example</span></div>

  <div class="copyright">2019 ©CORVEL RIDGE MANUFACTURING - All Rights Reserved</div>
</footer>

</body>
</html>
```